Exercise Physiologist needs a Brochure

I am Exercise Physiologist providing exercise therapy for a variety of conditions. I have a logo and recent business card design. I like the black background like the front of the business cards. I have attached the flyer information required. I have also attached a few photos however they do not have to be used, happy to have no photos at all.

Industry/Entity Type

Health And Wellness

Font styles to use
Sans Serif

Requirements
Must have
• Please also add instagram @morvalecare
Nice to have
• tri-fold brochure

```html
<!DOCTYPE html>
<html lang="en">
<head>
<meta charset="utf-8">
<title>Morvale Health – Exercise Physiology Flyer</title>
<link href="https://fonts.googleapis.com/css2?family=Montserrat:wght@400;500;600;700;800&family=Dancing+Script:wght@600&display=swap" rel="stylesheet">
<style>
  :root {
    --page-bg: #e9e6e2;
    --paper: #ffffff;
    --ink-dark: #1f2024;
    --ink-mid: #2c2e33;
    --brand-blue: #2f6fe0;
    --brand-blue-deep: #1f4fb4;
    --text-light: #e7e9ee;
    --text-muted: #b9bdc6;
    --rule: #4a4d55;
    --ink-black: #141414;
  }
  * { box-sizing: border-box; margin: 0; padding: 0; }
  html, body { width: 1200px; height: 918px; overflow: hidden; }
  body { background: var(--page-bg); font-family: "Montserrat", sans-serif; }

  .flyer {
    position: absolute; left: 275px; top: 0;
    width: 650px; height: 918px;
    background: var(--paper); overflow: hidden;
  }
  .hero-photo {
    position: absolute; left: 270px; top: 0; width: 380px; height: 320px;
    background: radial-gradient(ellipse at 55% 45%, #8fd3d0 0%, #c9b9a8 35%, #eef0f3 70%, #ffffff 100%);
  }
  .dark-panel { position: absolute; left: 0; top: 0; width: 650px; height: 918px; }

  .brand { position: absolute; left: 34px; top: 40px; display: flex; align-items: center; gap: 10px; }
  .brand-dot { width: 42px; height: 42px; border-radius: 50%; background: var(--brand-blue); }
  .brand-name { font-weight: 600; font-size: 30px; color: var(--brand-blue); letter-spacing: .5px; line-height: 1; }
  .brand-tag { display: block; font-size: 8px; font-weight: 500; letter-spacing: 1.5px; margin-top: 4px; }

  .practitioner { position: absolute; left: 34px; top: 130px; }
  .practitioner-name { font-weight: 800; font-size: 40px; color: var(--brand-blue); line-height: 1; }
  .practitioner-role { font-family: "Dancing Script", cursive; font-size: 30px; color: var(--ink-mid); margin-top: 2px; }
  .credentials { margin-top: 14px; font-weight: 700; font-size: 12.5px; color: var(--ink-black); line-height: 1.35; }

  .column-left { position: absolute; left: 34px; top: 392px; width: 290px; color: var(--text-light); }
  .column-right { position: absolute; left: 350px; top: 320px; width: 270px; color: var(--text-light); }

  .section-title { font-weight: 700; color: var(--brand-blue); font-size: 14px; margin: 16px 0 6px; }
  .lead-title { font-weight: 800; color: var(--brand-blue); font-size: 21px; margin-bottom: 8px; }
  .body-copy { font-size: 9.6px; line-height: 1.45; margin-bottom: 8px; color: var(--text-muted); }

  .conditions-title { font-weight: 800; color: var(--brand-blue); font-size: 16px; line-height: 1.1; }
  .conditions-sub { font-weight: 500; color: var(--brand-blue); font-size: 14px; display: block; }
  .conditions-list { list-style: none; margin-top: 12px; }
  .conditions-list li {
    position: relative; padding: 6px 0 6px 24px; font-size: 10.5px; font-weight: 700;
    border-bottom: 1px solid var(--rule);
  }
  .conditions-list li::before {
    content: ""; position: absolute; left: 2px; top: 7px; width: 12px; height: 12px;
    border-radius: 50%; background: var(--brand-blue); box-shadow: 0 0 0 2px #9fbef5 inset;
  }
  .closing { margin-top: 14px; padding-top: 8px; border-top: 1px solid var(--brand-blue); font-size: 11px; color: var(--brand-blue); font-weight: 600; line-height: 1.35; }
  .call-to-action { margin-top: 10px; font-weight: 700; font-size: 11.5px; color: #fff; }
  .contact-row { display: flex; align-items: center; gap: 8px; margin-top: 6px; }
  .contact-phone { font-weight: 800; font-size: 24px; color: #fff; }
  .contact-email { font-size: 13px; color: var(--text-light); }
  .contact-row svg { flex: none; }

  .footer {
    position: absolute; left: 0; bottom: 0; width: 650px; height: 50px;
    display: flex; align-items: center; gap: 18px; padding: 0 22px;
    font-size: 10px; color: var(--ink-mid); font-weight: 500;
  }
  .footer-item { display: flex; align-items: center; gap: 6px; white-space: nowrap; }
  .social-dot { width: 14px; height: 14px; border-radius: 50%; background: var(--brand-blue); display: inline-block; }
</style>
</head>
<body>
<main class="flyer">
  <div class="hero-photo" role="img" aria-label="Photo of an exercise physiologist guiding an older woman through a shoulder stretch"></div>

  <svg class="dark-panel" viewBox="0 0 650 918" aria-hidden="true">
    <defs>
      <linearGradient id="panelShade" x1="0" y1="0" x2="1" y2="1">
        <stop offset="0" stop-color="#2a2c31"/>
        <stop offset="1" stop-color="#18191c"/>
      </linearGradient>
    </defs>
    <path d="M0 392 C160 330 380 300 650 282 L650 868 L0 868 Z" fill="#1f4fb4"/>
    <path d="M0 408 C170 348 390 318 650 300 L650 868 L0 868 Z" fill="url(#panelShade)"/>
  </svg>

  <div class="brand">
    <span class="brand-dot"></span>
    <div class="brand-name">morvale<span class="brand-tag">HEALTH &amp; REHABILITATION</span></div>
  </div>

  <header class="practitioner">
    <h1 class="practitioner-name">Jenna Marlow</h1>
    <div class="practitioner-role">Exercise Physiologist</div>
    <p class="credentials">B.AppSci – Human Mvmt<br>Grad Dip – ExRehab<br>Cert IV – Training &amp; Assessment</p>
  </header>

  <section class="column-left">
    <h2 class="lead-title">Heal through Movement</h2>
    <p class="body-copy">Don't let the right exercise but the wrong technique hinder your recovery. Discover how important the correct exercise technique is to your success.</p>

    <h3 class="section-title">What is an Exercise Physiologist?</h3>
    <p class="body-copy">Exercise Physiologists are university educated health professionals trained to provide exercise therapy for pain and injury, pre and post surgery, mental health and chronic disease. They are registered providers with injury insurers, workplace schemes, public health cover and veterans' services and many private health funds.</p>

    <h3 class="section-title">How can I help you?</h3>
    <p class="body-copy">I have over 13 years of experience working as an Exercise Physiologist and have been working in the sport and fitness industry since 1996. I understand that everyone's health and exercise experience is unique and will tailor a program to suit you and your lifestyle.</p>
    <p class="body-copy">Managing your condition involves working with you to develop the best exercises and teaching you the correct technique essential to improve. Home and gym based programs can be provided.</p>
    <p class="body-copy">When appropriate I can also work with your current treating health practitioner to provide a holistic approach to your recovery.</p>
  </section>

  <section class="column-right">
    <h2 class="conditions-title">COMMON CONDITIONS<span class="conditions-sub">that benefit from exercise therapy</span></h2>
    <ul class="conditions-list">
      <li>Back pain</li>
      <li>Joint pain</li>
      <li>Pain relating to exercise</li>
      <li>Arthritis</li>
      <li>Anxiety relating to exercise</li>
      <li>Depression and Anxiety</li>
      <li>Chronic diseases such as diabetes, heart and lung disease.</li>
      <li>Motor vehicle accidents</li>
    </ul>
    <p class="closing">Performing the right exercise the wrong way can do more harm than good. I can teach you what, how and when to perform your tailored exercise program to get the best results.</p>
    <p class="call-to-action">Call or email me today to see how I can help you.</p>
    <div class="contact-row">
      <svg width="20" height="20" viewBox="0 0 24 24"><path d="M6.6 10.8a15 15 0 0 0 6.6 6.6l2.2-2.2c.3-.3.7-.4 1-.2 1.1.4 2.3.6 3.6.6.6 0 1 .4 1 1V20c0 .6-.4 1-1 1A17 17 0 0 1 3 4c0-.6.4-1 1-1h3.5c.6 0 1 .4 1 1 0 1.3.2 2.5.6 3.6.1.3 0 .7-.2 1z" fill="#2f6fe0"/></svg>
      <span class="contact-phone">0400 555 019</span>
    </div>
    <div class="contact-row">
      <svg width="20" height="16" viewBox="0 0 24 18"><rect x="1" y="1" width="22" height="16" rx="2" fill="#2f6fe0"/><path d="M2 2l10 8 10-8" stroke="#fff" stroke-width="1.8" fill="none"/></svg>
      <span class="contact-email">morvalecare@example.com</span>
    </div>
  </section>

  <footer class="footer">
    <span class="footer-item">
      <svg width="12" height="16" viewBox="0 0 12 16"><path d="M6 0a6 6 0 0 0-6 6c0 4.5 6 10 6 10s6-5.5 6-10a6 6 0 0 0-6-6zm0 8.2A2.2 2.2 0 1 1 6 3.8a2.2 2.2 0 0 1 0 4.4z" fill="#2f6fe0"/></svg>
      Gate 4, 18 Quarry Lane NORTH BAYSIDE (Harlow Fitness)
    </span>
    <span class="footer-item"><span class="social-dot"></span>@morvalecare</span>
    <span class="footer-item"><span class="social-dot"></span>morvale.example.com</span>
  </footer>
</main>
</body>
</html>
```